Local electrical company needs two flyers designed

We are a small local electrical contracting company and are in desperate need of a awasome flyer design to help grow our business

hi everyone.

please keep the logo off the front page.
it can go on the rear.

We are really trying to portray a angry/frustrated women BECAUSE her lights are broken.
not light globes

Target Market(s)

Home owners

Industry/Entity Type

Electrical

Font styles to use
Serif

Requirements
Nice to have

```html
<!DOCTYPE html>
<html lang="en">
<head>
<meta charset="utf-8">
<title>Lighting Replacement Flyer</title>
<link href="https://fonts.googleapis.com/css2?family=Ubuntu:wght@400;500;700&display=swap" rel="stylesheet">
<style>
  :root {
    --page-bg: #e9ece6;
    --green-deep: #0d5a2c;
    --green-mid: #1a7a3c;
    --red-band: #b81e32;
    --red-band-dark: #9c1628;
    --yellow: #ffd21f;
    --white: #ffffff;
    --photo-dark: #1e0e07;
    --photo-warm: #8a4a1c;
    --lamp-glow: #f2b25a;
    --hair: #4a2a18;
    --skin: #d9a07a;
    --shirt: #5a5a5e;
    --mascot-tone: #3b8a4a;
    --bulb-tone: #f3f1ea;
  }
  * { margin: 0; padding: 0; box-sizing: border-box; }
  html, body {
    width: 1200px; height: 896px; overflow: hidden;
    background: var(--page-bg);
    font-family: "Ubuntu", sans-serif;
  }
  .flyer {
    position: absolute; left: 40px; top: 50px;
    width: 1120px; height: 796px; overflow: hidden;
    background: radial-gradient(circle at 250px 260px, var(--green-mid) 0%, var(--green-deep) 75%);
    box-shadow: 0 4px 18px rgba(0,0,0,0.25);
  }
  .room-photo {
    position: absolute; left: 606px; top: 0; width: 514px; height: 796px;
    background:
      radial-gradient(circle at 400px 300px, var(--lamp-glow) 0%, rgba(242,178,90,0.35) 8%, rgba(0,0,0,0) 22%),
      radial-gradient(circle at 420px 420px, var(--photo-warm) 0%, var(--photo-dark) 65%);
    border-left: 6px solid var(--white);
  }
  .subject-photo {
    position: absolute; left: 528px; top: 255px; width: 478px; height: 541px;
    border-radius: 200px 200px 0 0;
    background:
      radial-gradient(ellipse 120px 150px at 235px 190px, var(--skin) 0%, #b87a55 70%, rgba(0,0,0,0) 100%),
      linear-gradient(180deg, var(--hair) 0%, var(--hair) 55%, var(--shirt) 70%, #3a3a3e 100%);
  }
  .headline-band {
    position: absolute; left: 128px; top: 80px; width: 992px; height: 185px;
    background: linear-gradient(180deg, var(--red-band) 0%, var(--red-band-dark) 100%);
  }
  .band-line {
    position: absolute; left: 0; width: 892px; text-align: center;
    font-weight: 700; line-height: 1; white-space: nowrap;
  }
  .band-question { top: 20px; font-size: 45px; color: var(--yellow); }
  .band-sub { top: 64px; font-size: 27px; color: var(--white); }
  .band-change { top: 112px; font-size: 46px; color: var(--yellow); }
  .mascot {
    position: absolute; left: 7px; top: 47px; width: 185px; height: 335px;
    background: linear-gradient(180deg, var(--mascot-tone), var(--green-deep));
    border-radius: 40px 40px 12px 12px;
  }
  .bulb {
    position: absolute; left: 984px; top: 47px; width: 128px; height: 293px;
    background: linear-gradient(180deg, var(--bulb-tone), #cfcac0);
    border-radius: 30px 30px 40px 40px;
  }
  .offer {
    position: absolute; left: 50px; top: 350px;
    color: var(--yellow); font-weight: 700; font-size: 82px; line-height: 77px;
    white-space: nowrap;
  }
  .offer .amount { color: var(--white); }
  .website {
    position: absolute; left: 26px; top: 736px;
    color: var(--white); font-size: 30px; font-weight: 400; white-space: nowrap;
  }
  .website strong { font-weight: 700; }
</style>
</head>
<body>
  <div class="flyer">
    <div class="room-photo" role="img" aria-label="Photo of a dim room lit by a single warm lamp"></div>
    <div class="subject-photo" role="img" aria-label="Photo of a frustrated young woman with long brown hair in a striped top, biting her fingers"></div>
    <div class="headline-band">
      <p class="band-line band-question">Is your lighting frustrating you?</p>
      <p class="band-line band-sub">Tired of coming home to lights that don’t always work?</p>
      <p class="band-line band-change">Thinking of a change?</p>
    </div>
    <div class="mascot" role="img" aria-label="Cartoon electrician superhero mascot pointing upward"></div>
    <div class="bulb" role="img" aria-label="Illustration of an energy-saving light bulb"></div>
    <p class="offer">SAVE <span class="amount">$25</span> off<br>your lighting<br>replacement</p>
    <p class="website">www.<strong>brightsparkhome</strong>.com.au</p>
  </div>
</body>
</html>
```